Zielgruppe
Wir produzieren Rebuilt Toner Kartuschen und vertreiben diese an privat Anwender und auch Firmen Kunden.
Unsere Produkte vertreiben wir unter einer eigenen Marke und auch neutral an Wiederverkäufer.
Jetzt suchen wir ein neues Produkt Aufkleber Design für die neutrale Ware (ohne Logo) soll aber trotzdem ein Wiedererkennungswert haben, aber nicht direkt auf uns zurückführen.
Ein Bild vom aktuellen Aufkleber, ist anbei.
Aufgabenstellung
Es soll ein universal Design sein welches wir für alle Produkte verwenden können. Somit keine Artikel Informationen im Design.
Als Text soll 'Rebuilt Cartridge' und 'Made in Germany' verwendet werden.
Das Design soll die hohe Qualität unterstreichen.
Die Hintergrundfarbe soll Schwarz sein.
Der Standard Aufkleber soll die Abmessungen 233x84mm haben.

```html
<!DOCTYPE html>
<html lang="en">
<head>
<meta charset="utf-8">
<title>Rebuilt Cartridge Label</title>
<link rel="stylesheet" href="https://fonts.googleapis.com/css2?family=Great+Vibes&family=Roboto:wght@300;400&display=swap">
<style>
  :root {
    --page: #ffffff;
    --label: #000000;
    --ink: #ffffff;
  }
  html, body {
    margin: 0;
    padding: 0;
    width: 1200px;
    height: 452px;
    overflow: hidden;
    background: var(--page);
  }
  .label-canvas {
    display: block;
    width: 1200px;
    height: 452px;
  }
  .label-body { fill: var(--label); }
  .label-frame,
  .label-corner {
    fill: none;
    stroke: var(--ink);
    stroke-width: 7;
    stroke-linejoin: miter;
  }
  .label-tagline {
    font-family: "Great Vibes", cursive;
    font-size: 56px;
    fill: var(--ink);
  }
  .label-title {
    font-family: "Roboto", sans-serif;
    font-weight: 400;
    font-size: 60px;
    letter-spacing: 1.5px;
    fill: var(--ink);
  }
  .label-origin {
    font-family: "Roboto", sans-serif;
    font-weight: 300;
    font-size: 17px;
    fill: var(--ink);
  }
</style>
</head>
<body>
<svg class="label-canvas" viewBox="0 0 1200 452" xmlns="http://www.w3.org/2000/svg">
  <rect class="label-body" x="25" y="21" width="1152" height="410"/>
  <polygon class="label-frame" points="49,42 1156,42 1156,262 946,406 49,406"/>
  <polygon class="label-corner" points="1156,288 1156,406 996,406"/>
  <text class="label-tagline" x="601" y="150" text-anchor="middle">Premium</text>
  <text class="label-title" x="601" y="256" text-anchor="middle">REBUILT CARTRIDGE</text>
  <text class="label-origin" x="601" y="334" text-anchor="middle">Made in Germany</text>
</svg>
</body>
</html>
```